Room Hire at The Willowmere Wellbeing & Talking House to encourage therapists to hire rooms from us

An A4 page for magazine printing and use to send online as well.

We want to attract therapists to come and hire our beautiful rooms. We have a soft green, cream and brown colour theme and a professional, warm, elegant style (we hope)
I've uploaded the previous advert we had done through art bazaar which was aimed at attracting therapy clients.

Target Market(s)

psychotherapists and physical therapists searching to hire consulting rooms

Industry/Entity Type

Font styles to use
Serif
Sans Serif
Script
Other font styles liked:
• Great Vibes

Colors
cadf82
abd037
9bcb3c
fdf9ce
fff3d1

Requirements
Must have
• Please include this text
• Website address
• Contact email address
• "The rooms are available to hire all day into the evenings and at weekends.
• There are 8 rooms, all suitable for Couples work, Individual Counselling or Supervision sessions. Some rooms are designed to be used by physical therapists as well. One of them is large enough to use for Family Therapy, to hold groups or to run Training Sessions for approximately fourteen people."
• The colour scheme to harmonise with our website theme colours and fonts - Colour RGA numbers
• Brown
• Red 65
• Green 53
• Blue 53
• Light green
• Red 129
• Green 157
• Blue 115
• www.wmth-harbridge.example.co.uk.
• Scrolling writing is Great Vibes by Plinko
• Be warm, calm, welcoming, professional styling, striking.
Nice to have
• Pictures of our rooms if we can provide enough quality for printing
Should not have
• Pictures of people touching each other.
• Not be too busy or angular

```html
<!DOCTYPE html>
<html lang="en">
<head>
<meta charset="utf-8">
<title>Room Hire – The Willowmere Wellbeing &amp; Talking House</title>
<link rel="stylesheet" href="https://fonts.googleapis.com/css2?family=Great+Vibes&family=Lato:wght@400;700&display=swap">
<style>
  :root {
    --backdrop: #e9e6df;
    --paper: #ffffff;
    --green-light: #abd037;
    --green-mid: #9bcb3c;
    --green-sage: #819d73;
    --peach: #f7d7a6;
    --apricot: #f2b27a;
    --salmon: #e9856c;
    --brown: #413535;
    --body-grey: #5a5552;
    --photo-cream: #f3e3b4;
    --photo-wood: #c9954f;
  }
  * { margin: 0; padding: 0; box-sizing: border-box; }
  html, body { width: 1200px; height: 1200px; overflow: hidden; }
  body { background: var(--backdrop); font-family: "Lato", sans-serif; position: relative; }

  .advert {
    position: absolute; left: 200px; top: 34px;
    width: 800px; height: 1131px;
    background: var(--paper); overflow: hidden;
    box-shadow: 0 6px 24px rgba(0,0,0,.18);
  }
  .room-photo {
    position: absolute; left: 0; top: 0; width: 800px; height: 560px;
    background: linear-gradient(160deg, #fbf1d2 0%, var(--photo-cream) 40%, #e6c48a 70%, var(--photo-wood) 100%);
  }
  .waves, .footer-band { position: absolute; left: 0; top: 0; width: 800px; height: 1131px; }

  .brand { position: absolute; left: 0; width: 800px; top: 538px; text-align: center; }
  .brand-dot {
    display: block; width: 52px; height: 52px; margin: 0 auto 22px;
    border-radius: 50%; background: var(--green-sage);
  }
  .brand-name { font-size: 19px; font-weight: 400; color: var(--green-sage); letter-spacing: .3px; }

  .headline {
    position: absolute; left: 0; top: 690px; width: 800px; text-align: center;
    font-family: "Great Vibes", cursive; font-weight: 400;
    font-size: 56px; line-height: 54px; color: var(--brown);
  }
  .details {
    position: absolute; left: 62px; top: 812px; width: 676px; text-align: center;
    font-size: 16.5px; line-height: 22.5px; color: var(--body-grey);
  }

  .small-photo {
    position: absolute; left: 81px; top: 912px; width: 262px; height: 262px;
    border-radius: 50%; background: var(--paper);
    border: 8px solid var(--green-sage);
    padding: 6px;
  }
  .small-photo-fill {
    width: 100%; height: 100%; border-radius: 50%;
    background: linear-gradient(180deg, #f4ecd8 0%, #e8dcc0 45%, #7a3b2e 70%, #d9c6a0 100%);
  }

  .contact {
    position: absolute; right: 48px; top: 1002px; text-align: right; color: #fff;
  }
  .contact-phone { font-size: 26px; font-weight: 700; line-height: 34px; }
  .contact-line { font-size: 15px; line-height: 26px; }
  .contact svg { vertical-align: -2px; margin-right: 6px; }
</style>
</head>
<body>
  <main class="advert">
    <div class="room-photo" role="img" aria-label="Photograph of a bright counselling room with a cream tub chair, wooden sideboard, side table and window plants"></div>

    <svg class="waves" viewBox="0 0 958 1356" preserveAspectRatio="none" aria-hidden="true">
      <path d="M0,700 C30,680 70,655 120,640 C300,600 450,660 600,680 C760,700 900,650 958,590 L958,1356 L0,1356 Z" fill="var(--paper)"/>
      <path d="M0,470 C160,440 360,455 470,545 L440,555 C330,490 160,485 0,520 Z" fill="var(--peach)"/>
      <path d="M0,520 C160,485 330,490 440,555 L420,570 C300,515 150,520 0,560 Z" fill="var(--apricot)"/>
      <path d="M0,580 C180,500 380,510 520,590 C650,660 800,660 900,610 C930,595 950,570 958,540 L958,590 C900,650 760,700 600,680 C450,660 300,600 120,640 C70,655 30,680 0,700 Z" fill="var(--green-light)"/>
      <path d="M0,640 C180,560 380,560 520,620 C640,670 780,680 958,590 C900,650 760,700 600,680 C450,660 300,600 120,640 C70,655 30,680 0,700 Z" fill="var(--green-mid)"/>
      <path d="M0,800 C60,705 180,625 340,590 C200,640 80,720 0,830 Z" fill="var(--salmon)"/>
      <path d="M958,560 C930,630 850,655 700,665 C840,680 930,650 958,610 Z" fill="var(--apricot)"/>
      <path d="M958,530 C920,600 860,630 760,645 C860,650 930,620 958,575 Z" fill="var(--peach)"/>
    </svg>

    <svg class="footer-band" viewBox="0 0 800 1131" aria-hidden="true">
      <path d="M0,1018 C50,1036 100,1050 150,1058" stroke="var(--salmon)" stroke-width="5" fill="none"/>
      <path d="M0,1040 C100,1080 250,1110 380,1110 C440,1110 480,990 800,985 L800,1131 L0,1131 Z" fill="var(--green-sage)"/>
    </svg>

    <div class="brand">
      <span class="brand-dot"></span>
      <p class="brand-name">The Willowmere Wellbeing &amp; Talking House</p>
    </div>

    <h1 class="headline">The rooms are available to hire all day<br>into the evenings and at weekends</h1>

    <p class="details">There are 8 rooms, all suitable for Couples work, Individual Counselling or Supervision sessions. Some rooms are designed to be used by physical therapists as well. One of them is large enough to use for Family Therapy, to hold groups or to run Training Sessions for approximately fourteen people.</p>

    <div class="small-photo">
      <div class="small-photo-fill" role="img" aria-label="Photograph of a consulting room with two leather armchairs, a sideboard and a patterned rug"></div>
    </div>

    <div class="contact">
      <p class="contact-phone"><svg width="18" height="18" viewBox="0 0 24 24"><path d="M6.6 10.8a15.1 15.1 0 0 0 6.6 6.6l2.2-2.2a1 1 0 0 1 1-.25 11.4 11.4 0 0 0 3.6.57 1 1 0 0 1 1 1V20a1 1 0 0 1-1 1A17 17 0 0 1 3 4a1 1 0 0 1 1-1h3.5a1 1 0 0 1 1 1c0 1.25.2 2.45.57 3.57a1 1 0 0 1-.25 1z" fill="none" stroke="#fff" stroke-width="2"/></svg>01632 960418</p>
      <p class="contact-line"><svg width="15" height="15" viewBox="0 0 24 24"><circle cx="12" cy="12" r="10" fill="none" stroke="#fff" stroke-width="2"/><path d="M2 12h20M12 2c3 3 3 17 0 20M12 2c-3 3-3 17 0 20" fill="none" stroke="#fff" stroke-width="1.6"/></svg>www.wmth-harbridge.example.co.uk</p>
      <p class="contact-line"><svg width="15" height="12" viewBox="0 0 24 18"><rect x="1" y="1" width="22" height="16" fill="none" stroke="#fff" stroke-width="2"/><path d="M1 1l11 9 11-9" fill="none" stroke="#fff" stroke-width="2"/></svg>rowena@wmth-harbridge.example.co.uk</p>
    </div>
  </main>
</body>
</html>
```